Summit Mineral Wealth Builder Plan

I want a professional design for a new investment program that we have designed for prospecting new prospects. We have a company logo and the content that we would like for the brochure but we would like and design structure and graphics to help compliment the content. I am attaching a rough draft of the brochure that has some

Target Market(s)

Anyone looking for hard assets, inflation hedge, cash flow investments.

```html
<!DOCTYPE html>
<html lang="en">
<head>
<meta charset="UTF-8">
<title>Summit Mineral Wealth Builder Plan</title>
<link rel="stylesheet" href="https://fonts.googleapis.com/css2?family=EB+Garamond:wght@400;700&family=Libre+Caslon+Text:wght@400&family=Tinos&display=swap">
<style>
  :root {
    --paper: #eeeeeb;
    --ink: #1c1c1c;
    --muted: #333333;
    --brand-green: #3f6b3a;
    --bill-light: #c9d3b0;
    --bill-mid: #8fa37a;
    --bill-dark: #4f6a45;
  }
  * { margin: 0; padding: 0; box-sizing: border-box; }
  html, body { width: 848px; height: 1200px; overflow: hidden; }
  body { background: var(--paper); color: var(--ink); }
  .brochure-cover { position: relative; width: 848px; height: 1200px; background: var(--paper); }
  .company-label {
    position: absolute; top: 60px; left: 0; width: 100%;
    text-align: center; font-family: "Tinos", serif; font-size: 15px; color: var(--ink);
  }
  .hero-visual {
    position: absolute; left: 205px; top: 198px; width: 510px; height: 200px;
    border-radius: 10px;
    background: radial-gradient(ellipse at 55% 45%, var(--bill-light) 0%, var(--bill-mid) 55%, var(--bill-dark) 100%);
    box-shadow: 0 0 0 6px #f7f7f4;
  }
  .program-title {
    position: absolute; top: 482px; left: 0; width: 100%; text-align: center;
    font-family: "Libre Caslon Text", serif; font-weight: 400; color: var(--ink);
  }
  .program-title .title-lead { display: block; font-size: 46px; line-height: 56px; }
  .program-title .title-main { display: block; font-size: 66px; line-height: 64px; }
  .program-intro {
    position: absolute; top: 690px; left: 154px; width: 540px; text-align: center;
    font-family: "EB Garamond", serif; font-size: 23px; line-height: 34px; color: var(--ink);
  }
  .program-intro strong { font-weight: 700; }
  .brand-mark {
    position: absolute; top: 975px; left: 0; width: 100%;
    display: flex; align-items: center; justify-content: center; gap: 10px;
  }
  .brand-mark .brand-dot { width: 14px; height: 14px; border-radius: 50%; background: var(--brand-green); }
  .brand-mark .brand-name {
    font-family: "EB Garamond", serif; font-size: 24px; font-weight: 400; color: var(--brand-green);
  }
  .contact-block {
    position: absolute; top: 1084px; left: 0; width: 100%; text-align: center;
    font-family: "Tinos", serif; font-size: 12px; line-height: 17.5px; color: var(--muted);
    font-style: normal;
  }
</style>
</head>
<body>
  <main class="brochure-cover">
    <p class="company-label">Summit Mineral Holdings, LLC</p>

    <div class="hero-visual" role="img" aria-label="Torn paper revealing a close-up of green banknote engraving"></div>

    <h1 class="program-title">
      <span class="title-lead">Summit Mineral</span>
      <span class="title-main">Wealth Builder</span>
      <span class="title-main">Plan</span>
    </h1>

    <p class="program-intro">
      What should investors do to in this uncertain period to
      <strong>profit from the evolving energy transition</strong> and protect
      themselves from what appears to be an <strong>inevitable wave of inflation</strong>?
      We have one asset class and a business opportunity behind it that can address both.
    </p>

    <div class="brand-mark">
      <span class="brand-dot"></span>
      <span class="brand-name">Summit Mineral Holdings, LLC</span>
    </div>

    <address class="contact-block">
      4820 Cedar Crest Dr. #118<br>
      Allen, TX 75013<br>
      info@summitmineralco.com<br>
      214-555-0182
    </address>
  </main>
</body>
</html>
```